Tango Holiday Website Needs a Header Design

I'm looking for a talented designer to create an attractive header for my website: http://brightmerengue.de/. I only want a Header Design. The website and everything else should stay the same.
We will be offering vacations for people who want to come to Tenerife to learn and dance Argentine tango. There will be lessons during the day and dancing during the evening. Tenerife is a warm and sunny destination.
The header should blend in well with the background and the images. The current dimentions fo the header is 960 x 160 pixels.
I like the design on a similar website: http://velosacumbia.de/.
Here are some images on google for tango holiday that might help: http://qlnk.to/7kRw41P
I'm flexible with colours and am looking forward to your suggestions.
Tango dancers between the ages of 40 and 65

```html
<!DOCTYPE html>
<html lang="en">
<head>
<meta charset="utf-8">
<title>Bright Merengue – Tango Holidays in Tenerife</title>
<link rel="stylesheet" href="https://fonts.googleapis.com/css2?family=Great+Vibes&family=Cormorant+Garamond:wght@500&display=swap">
<style>
  :root {
    --coral: #fb5a5a;
    --coral-light: #fd7b7b;
    --coral-pale: #fe9a9a;
    --coral-deep: #f44c4c;
    --paper: #ffffff;
    --ink: #111111;
    --accent-text: #e24a4a;
    --silhouette: #141414;
  }
  html, body {
    margin: 0;
    padding: 0;
    width: 1200px;
    height: 200px;
    overflow: hidden;
    background: var(--paper);
  }
  .site-header {
    position: relative;
    width: 1200px;
    height: 200px;
    overflow: hidden;
  }
  .header-backdrop {
    position: absolute;
    inset: 0;
    width: 1200px;
    height: 200px;
  }
  .band-coral { fill: var(--coral); }
  .band-coral-light { fill: var(--coral-light); }
  .band-coral-pale { fill: var(--coral-pale); }
  .band-coral-deep { fill: var(--coral-deep); }
  .band-paper { fill: var(--paper); }
  .dancers-silhouette { fill: var(--silhouette); }

  .brand {
    position: absolute;
    left: 440px;
    top: 24px;
    width: 600px;
  }
  .brand-name {
    margin: 0;
    font-family: "Great Vibes", cursive;
    font-weight: 400;
    font-size: 82px;
    line-height: 1;
    color: var(--ink);
    letter-spacing: 1px;
    white-space: nowrap;
  }
  .brand-tagline {
    margin: 4px 0 0 4px;
    font-family: "Cormorant Garamond", serif;
    font-weight: 500;
    font-size: 22px;
    font-variant: small-caps;
    letter-spacing: 1.5px;
    color: var(--accent-text);
    white-space: nowrap;
  }
</style>
</head>
<body>
  <header class="site-header">
    <svg class="header-backdrop" viewBox="0 0 1200 200" aria-hidden="false">
      <!-- left coral field -->
      <rect class="band-coral" x="0" y="0" width="520" height="200"/>
      <polygon class="band-coral-deep" points="0,0 160,0 0,160"/>
      <polygon class="band-coral-light" points="160,0 330,0 130,200 0,200 0,160"/>
      <polygon class="band-coral-pale" points="330,0 494,0 294,200 130,200"/>
      <!-- centre white band -->
      <polygon class="band-paper" points="494,0 1180,0 955,200 294,200"/>
      <!-- right coral field -->
      <polygon class="band-coral-light" points="1180,0 1200,0 1200,200 955,200"/>
      <polygon class="band-coral" points="1200,40 1200,200 1040,200"/>
      <!-- dancers illustration area -->
      <rect class="dancers-silhouette" x="122" y="14" width="150" height="186" rx="48"
            role="img" aria-label="Silhouette of a tango couple in a close embrace"/>
    </svg>

    <div class="brand">
      <h1 class="brand-name">Bright Merengue</h1>
      <p class="brand-tagline">Tango Holidays in Tenerife</p>
    </div>
  </header>
</body>
</html>
```